Tallow Creek Partners needs an email sign off and professional power point template

Newly formed company and we require:1. graphic email signature on our email , and2.a professional powerpoint template (title page and sub pages) and revamp of the attached powerpoint presentation I have uploaded our business car design (logo and contact details ) and a current powerpoint template we are currently working with. Also a brief of how we operateOur mantra is Discover, Develop, Deliver.

Target Market(s)

multinationals and mid size SME's requiring help to grown new markets or geographies for their business.

Colors
000000

Requirements
Must have
• the mantra..our phases of engagement around assisting clients is:
• 1. Discover
• 2. Develop
• 3. Deliver
Nice to have
• we differentiate ourselves form consultant by actually executing the plan for them (i.e. is the delivery phase)

```html
<!DOCTYPE html>
<html lang="en">
<head>
<meta charset="utf-8">
<title>Tallow Creek Partners – Slide Template</title>
<link href="https://fonts.googleapis.com/css2?family=Open+Sans:ital,wght@0,400;0,700;1,700&family=Roboto+Condensed:wght@700&family=Arimo:wght@400;700&display=swap" rel="stylesheet">
<style>
:root{
  --navy:#17243f;
  --navy-2:#1f3358;
  --band:#c9d3e0;
  --chev:#dbe5f2;
  --chev-text:#2b3b57;
  --accent:#2f63b0;
  --teal:#1a9cc9;
  --ink:#111;
  --grey:#b5b5b5;
  --line:#8a8a8a;
}
*{box-sizing:border-box;margin:0;padding:0}
html,body{width:1200px;height:848px;overflow:hidden;background:#fff}
body{position:relative;font-family:"Arimo",Arial,sans-serif;color:var(--ink)}
.slide{position:absolute;width:366px;height:252px;background:#fff;overflow:hidden;box-shadow:0 0 0 1px #eee}
.c1{left:29px}.c2{left:416px}.c3{left:805px}
.r1{top:27px}.r2{top:299px}.r3{top:572px}

.bar{position:absolute;left:0;top:0;height:20px;background:var(--navy);
  clip-path:polygon(0 0,100% 0,calc(100% - 34px) 100%,0 100%);
  color:#fff;font-family:"Roboto Condensed",Arial Narrow,sans-serif;font-size:10.5px;line-height:20px;padding-left:8px;white-space:nowrap}
.bar.small{font-size:8px;height:16px;line-height:16px;padding-left:6px}

.footer{position:absolute;left:0;bottom:0;width:366px;height:18px}
.footer svg{position:absolute;left:0;top:0}
.footer .mantra{position:absolute;left:4px;bottom:1px;font-size:4.5px;letter-spacing:2.6px;color:#fff;font-weight:700}
.footer .page{position:absolute;right:4px;bottom:1px;font-size:4.5px;color:#fff}

.cover-band{position:absolute;left:0;top:0;width:366px;height:20px;background:var(--navy)}
.cover-mark{position:absolute;left:0;top:0;width:77px;height:79px;background:var(--navy);
  clip-path:polygon(0 0,100% 0,100% 78%,78% 100%,0 100%);
  color:#fff;font-weight:700;font-size:11px;line-height:13px;padding:24px 0 0 10px}
.cover-title{position:absolute;left:0;width:366px;top:119px;text-align:center;font-family:"Open Sans",sans-serif;font-weight:700;font-size:19px;color:var(--navy-2)}
.cover-sub{position:absolute;left:0;width:366px;top:144px;text-align:center;font-family:"Open Sans",sans-serif;font-style:italic;font-weight:700;font-size:8px;color:var(--navy-2)}
.cover-date{position:absolute;left:93px;top:203px;font-family:"Open Sans",sans-serif;font-weight:700;font-size:18px;color:var(--grey)}
.cover-date sup{font-size:10px;font-weight:400;vertical-align:6px}

.note{position:absolute;left:68px;top:84px;width:236px;height:34px;border:1px solid var(--line);
  font-size:7.5px;font-weight:700;text-align:center;display:flex;align-items:center;justify-content:center;padding:0 12px;line-height:1.25}

.box{position:absolute;border:1px solid #9a9a9a;background:#fafafa;box-shadow:1px 1px 2px rgba(0,0,0,.25);
  font-size:5.8px;line-height:1.2;text-align:center;display:flex;align-items:center;justify-content:center;padding:1px}
.ghost{position:absolute;font-family:"Open Sans",sans-serif;font-style:italic;font-weight:700;font-size:9px;line-height:11px;color:var(--accent)}

.inset{position:absolute;left:103px;top:70px;width:263px;height:182px;background:#fff;box-shadow:-2px 2px 5px rgba(0,0,0,.3)}
.inset .footer{width:263px;height:12px}
.chev{position:absolute;background:var(--chev);color:var(--chev-text);font-size:5.5px;line-height:1.2;text-align:center;
  display:flex;align-items:center;justify-content:center;padding:0 8px}
.pr{clip-path:polygon(0 0,88% 0,100% 50%,88% 100%,0 100%)}
.pl{clip-path:polygon(12% 0,100% 0,100% 100%,12% 100%,0 50%)}
.pd{clip-path:polygon(0 0,100% 0,100% 82%,50% 100%,0 82%)}
.pu{clip-path:polygon(0 18%,50% 0,100% 18%,100% 100%,0 100%)}
.hub{position:absolute;font-family:"Open Sans",sans-serif;font-style:italic;font-weight:700;font-size:8.5px;line-height:10px;color:var(--accent);text-align:center}

.heading{position:absolute;left:15px;top:52px;font-size:12.5px;font-weight:400;letter-spacing:.2px}
.list{position:absolute;left:15px;top:86px;width:340px;font-size:9.3px;line-height:11.3px;list-style:none}
.list li{display:flex}
.list li span:first-child{width:20px;flex:none}
.u{text-decoration:underline;font-size:11px}

.tool-mark{position:absolute;left:14px;top:70px;width:76px;height:110px;display:flex;align-items:center;justify-content:center;
  font-weight:700;font-size:12px;color:var(--navy);text-align:center;line-height:14px}
.tool{position:absolute;font-weight:700;white-space:nowrap}
.tool-desc{position:absolute;left:206px;font-size:6.5px;line-height:1.3;text-align:center;width:150px}
</style>
</head>
<body>

<section class="slide c1 r1">
  <div class="cover-band"></div>
  <div class="cover-mark">Tallow<br>Creek</div>
  <h1 class="cover-title">Tallow Creek Partners</h1>
  <p class="cover-sub">Discover, Develop, Deliver</p>
  <p class="cover-date"><sup>12th</sup> December 2018</p>
  <div class="footer"><svg width="366" height="18"><rect y="10" width="366" height="8" fill="#c9d3e0"/><polygon points="328,18 366,18 366,0" fill="#17243f"/></svg><span class="mantra">DISCOVER DEVELOP DELIVER</span><span class="page">1</span></div>
</section>

<section class="slide c2 r1">
  <div class="cover-band"></div>
  <svg width="366" height="252" style="position:absolute;left:0;top:0" role="img" aria-label="Discover, Develop, Deliver around You">
    <defs>
      <path id="arcL" d="M113,122 A35,35 0 0 1 160,72"/>
      <path id="arcR" d="M206,72 A35,35 0 0 1 253,122"/>
    </defs>
    <g fill="none" stroke="#0e1525" stroke-width="4">
      <circle cx="143" cy="103" r="41"/>
      <circle cx="223" cy="103" r="41"/>
      <circle cx="183" cy="162" r="44"/>
    </g>
    <circle cx="183" cy="126" r="15" fill="#1a9cc9" stroke="#fff" stroke-width="2"/>
    <text x="183" y="130" text-anchor="middle" font-family="Roboto Condensed, sans-serif" font-weight="700" font-size="11" fill="#fff">YOU</text>
    <text font-family="Roboto Condensed, sans-serif" font-weight="700" font-size="12" fill="#0e1525"><textPath href="#arcL">DEVELOP</textPath></text>
    <text font-family="Roboto Condensed, sans-serif" font-weight="700" font-size="12" fill="#0e1525"><textPath href="#arcR">DELIVER</textPath></text>
    <text x="183" y="175" text-anchor="middle" font-family="Roboto Condensed, sans-serif" font-weight="700" font-size="14" fill="#0e1525">DISCOVER</text>
  </svg>
  <div class="footer"><svg width="366" height="18"><rect y="10" width="366" height="8" fill="#c9d3e0"/><polygon points="328,18 366,18 366,0" fill="#17243f"/></svg><span class="mantra">DISCOVER DEVELOP DELIVER</span><span class="page">2</span></div>
</section>

<section class="slide c3 r1">
  <div class="bar" style="width:322px">Directors</div>
  <div class="note">Would like a slide where we can insert all 3 directors experience</div>
  <div class="footer"><svg width="366" height="18"><rect y="10" width="366" height="8" fill="#c9d3e0"/><polygon points="328,18 366,18 366,0" fill="#17243f"/></svg><span class="mantra">DISCOVER DEVELOP DELIVER</span><span class="page">3</span></div>
</section>

<section class="slide c1 r2">
  <div class="bar small" style="width:229px">Opportunity Planning Process</div>
  <svg width="366" height="252" style="position:absolute;left:0;top:0">
    <g fill="#17243f">
      <polygon points="82,51 96,51 96,48 102,54 96,60 96,57 82,57"/>
      <polygon points="159,51 173,51 173,48 179,54 173,60 173,57 159,57"/>
      <polygon points="104,142 90,142 90,139 84,145 90,151 90,148 104,148"/>
    </g>
  </svg>
  <div class="box" style="left:26px;top:39px;width:51px;height:30px">Identify Opportunity</div>
  <div class="box" style="left:103px;top:39px;width:52px;height:30px">Qualify Opportunity (Discover)</div>
  <div class="box" style="left:181px;top:36px;width:55px;height:33px">Identify Key Individuals of Influence to Decision Process</div>
  <div class="box" style="left:26px;top:128px;width:51px;height:30px">Negotiate and Sign</div>
  <div class="ghost" style="left:78px;top:87px">Disco<br>Devel<br>Deliv</div>
  <div class="inset">
    <div class="bar small" style="width:229px">Opportunity Planning Process</div>
    <div class="chev pr" style="left:19px;top:32px;width:80px;height:35px">Identify Opportunity</div>
    <div class="chev pr" style="left:98px;top:32px;width:80px;height:35px">Qualify Opportunity (Discover)</div>
    <div class="chev pd" style="left:177px;top:32px;width:71px;height:38px">Identify Key Individuals of Influence to Decision Process</div>
    <div class="hub" style="left:40px;top:84px;width:60px">Discover<br>Develop<br>Deliver</div>
    <div class="chev pd" style="left:177px;top:79px;width:71px;height:38px">Develop &amp; Implement Sales Strategy &amp; Plan</div>
    <div class="chev" style="left:19px;top:125px;width:78px;height:36px">Negotiate and Sign</div>
    <div class="chev pl" style="left:96px;top:125px;width:80px;height:36px">Execute Plan And Deliver Proposal</div>
    <div class="chev pl" style="left:175px;top:125px;width:73px;height:36px">Align &amp; Develop Relationships with Key people of Influence</div>
    <div class="footer"><svg width="263" height="12"><rect y="6" width="263" height="6" fill="#c9d3e0"/><polygon points="235,12 263,12 263,0" fill="#17243f"/></svg><span class="mantra" style="font-size:3.5px">DISCOVER DEVELOP DELIVER</span><span class="page" style="font-size:3.5px">4</span></div>
  </div>
</section>

<section class="slide c2 r2">
  <div class="bar small" style="width:222px">Market Region &amp; Account Planning Process</div>
  <svg width="366" height="252" style="position:absolute;left:0;top:0">
    <g fill="#17243f">
      <polygon points="81,51 95,51 95,48 101,54 95,60 95,57 81,57"/>
      <polygon points="170,51 184,51 184,48 190,54 184,60 184,57 170,57"/>
      <polygon points="44,80 44,90 41,90 47,96 53,90 50,90 50,80" transform="rotate(180 47 88)"/>
      <polygon points="44,128 44,138 41,138 47,144 53,138 50,138 50,128" transform="rotate(180 47 136)"/>
      <polygon points="100,140 86,140 86,137 80,143 86,149 86,146 100,146"/>
    </g>
  </svg>
  <div class="box" style="left:17px;top:38px;width:57px;height:31px">Segment your Regions into Accounts</div>
  <div class="box" style="left:111px;top:38px;width:57px;height:31px">Analyse your Current Business</div>
  <div class="box" style="left:192px;top:38px;width:57px;height:31px">Identify "New" Opportunities</div>
  <div class="box" style="left:17px;top:97px;width:57px;height:31px">Measure and Monitor Progress</div>
  <div class="box" style="left:17px;top:145px;width:57px;height:31px">Implement the Strategy Action Plan</div>
  <div class="inset">
    <div class="bar small" style="width:232px">Market Region &amp; Account Planning Process</div>
    <div class="chev pr" style="left:19px;top:32px;width:80px;height:35px">Segment your Regions into Accounts</div>
    <div class="chev pr" style="left:98px;top:32px;width:80px;height:35px">Analyze your Current Business</div>
    <div class="chev pd" style="left:177px;top:32px;width:71px;height:38px">Identify "New" Opportunities</div>
    <div class="chev pu" style="left:19px;top:77px;width:78px;height:38px">Measure and Monitor Progress</div>
    <div class="hub" style="left:103px;top:84px;width:70px">It's all about your Customer…</div>
    <div class="chev pd" style="left:177px;top:79px;width:71px;height:38px">Create an Account Strategy &amp; Plan</div>
    <div class="chev pu" style="left:19px;top:123px;width:78px;height:38px">Implement the Strategy Action Plan</div>
    <div class="chev pl" style="left:96px;top:125px;width:80px;height:36px">Manage the Key Relationships (Walk the Halls)</div>
    <div class="chev pl" style="left:175px;top:125px;width:73px;height:36px">Select Strategy &amp; Market to the Account</div>
    <div class="footer"><svg width="263" height="12"><rect y="6" width="263" height="6" fill="#c9d3e0"/><polygon points="235,12 263,12 263,0" fill="#17243f"/></svg><span class="mantra" style="font-size:3.5px">DISCOVER DEVELOP DELIVER</span><span class="page" style="font-size:3.5px">5</span></div>
  </div>
</section>

<section class="slide c3 r2">
  <div class="bar" style="width:322px">Discover – Analyze your Business Territory &amp; Market Segment</div>
  <h2 class="heading">DISCOVER</h2>
  <ol class="list">
    <li><span>1.</span><span>Analyse Your Business &amp; all of its current Sales Territory(s)</span></li>
    <li><span>2.</span><span>Understand What Drives Customers to Buy.</span></li>
    <li><span>3.</span><span>Understand Your Customers Business Drivers and Objectives they need to achieve.</span></li>
    <li><span>4.</span><span>Identify what your Customers Clients need ( Perceived / Unperceived)</span></li>
    <li><span>5.</span><span>Clarify Your Strengths, Weaknesses, Opportunities and Threats (SWOT).</span></li>
    <li><span>6.</span><span>Clarify Your <span class="u">COMPETITORS</span> Strengths, Weaknesses, Opportunities and Threats (SWOT).</span></li>
    <li><span>7.</span><span>Clarify Your CUSTOMERS Strengths, Weaknesses, Opportunities and Threats (SWOT).</span></li>
  </ol>
  <div class="footer"><svg width="366" height="18"><rect y="10" width="366" height="8" fill="#c9d3e0"/><polygon points="328,18 366,18 366,0" fill="#17243f"/></svg><span class="mantra">DISCOVER DEVELOP DELIVER</span><span class="page">6</span></div>
</section>

<section class="slide c1 r3">
  <div class="bar" style="width:320px">Develop – Determine Objectives &amp; Create Strategies</div>
  <h2 class="heading" style="left:18px">DEVELOP</h2>
  <ol class="list" style="left:18px;width:320px">
    <li><span>1.</span><span>Determine Your Objectives</span></li>
    <li><span>2.</span><span>Develop Strategies to Accomplish Your Goals</span></li>
    <li><span>3.</span><span>Engage the Resources You Need.</span></li>
    <li><span>4.</span><span>Create an Influencing Strategy to develop key Relationships.</span></li>
    <li><span>5.</span><span>Create a Marketing Strategy – Create Alignment with the Sales and Marketing teams.</span></li>
    <li><span>6.</span><span>Create a complete Action Plan – Strategy and Tactics.</span></li>
    <li><span>7.</span><span>Develop the Project Management discipline to manage the full life cycle of your Relationship with the Customer.</span></li>
  </ol>
  <div class="footer"><svg width="366" height="18"><rect y="10" width="366" height="8" fill="#c9d3e0"/><polygon points="328,18 366,18 366,0" fill="#17243f"/></svg><span class="mantra">DISCOVER DEVELOP DELIVER</span><span class="page">7</span></div>
</section>

<section class="slide c2 r3">
  <div class="bar" style="width:322px">Discover – Analyze your Business Territory &amp; Market Segment</div>
  <h2 class="heading" style="left:20px">DELIVER</h2>
  <ol class="list" style="left:16px;width:330px">
    <li><span>1.</span><span>Work Your Plan.</span></li>
    <li><span>2.</span><span>Measure &amp; Monitor progress, Stakeholder alignment and capture growth through your Project Management discipline</span></li>
    <li><span>3.</span><span>Deepen your Client Relationship to leverage future opportunity as a Partner.</span></li>
  </ol>
  <div class="footer"><svg width="366" height="18"><rect y="10" width="366" height="8" fill="#c9d3e0"/><polygon points="328,18 366,18 366,0" fill="#17243f"/></svg><span class="mantra">DISCOVER DEVELOP DELIVER</span><span class="page">8</span></div>
</section>

<section class="slide c3 r3">
  <div class="bar" style="width:305px">Current Opportunity &amp; Account Management Process</div>
  <div class="tool-mark">Tallow<br>Creek</div>
  <svg width="366" height="252" style="position:absolute;left:0;top:0">
    <g stroke="#17243f" stroke-width="3.5" fill="#17243f">
      <line x1="86" y1="84" x2="106" y2="62"/>
      <polygon points="111,57 98,61 107,70" stroke="none"/>
      <line x1="86" y1="126" x2="106" y2="126"/>
      <polygon points="113,126 104,120 104,132" stroke="none"/>
      <line x1="86" y1="166" x2="106" y2="186"/>
      <polygon points="112,192 107,180 99,189" stroke="none"/>
    </g>
  </svg>
  <div class="tool" style="left:122px;top:34px;width:66px;height:27px;background:#222;color:#fff;font-size:12px;display:flex;align-items:center;justify-content:center">Dealflow</div>
  <div class="tool-desc" style="top:36px">Client CRM, Account Management Tool: All Opportunities, Deal Progress, Sales Forecasting, Tender or Deal management.</div>
  <div class="tool" style="left:118px;top:115px;font-size:15px;color:var(--teal)">Pitchwell</div>
  <div class="tool-desc" style="top:118px">For All Tallow BD or Client Templated Formal Proposals and Sales Contract / T&amp;C's Management.</div>
  <div class="tool" style="left:122px;top:186px;font-size:12px;color:var(--teal);display:flex;align-items:center;gap:4px"><span style="width:10px;height:10px;border-radius:50%;background:var(--teal);display:inline-block"></span>Ledgerly</div>
  <div class="tool-desc" style="top:188px">Client Information, Invoicing and Full Suite Business Accounting Software</div>
  <div class="footer"><svg width="366" height="18"><rect y="10" width="366" height="8" fill="#c9d3e0"/><polygon points="328,18 366,18 366,0" fill="#17243f"/></svg><span class="mantra">DISCOVER DEVELOP DELIVER</span><span class="page">9</span></div>
</section>

</body>
</html>
```